I need a cd cover my CD. The cd is about my journey in my recovery from addiction. The name of the CD is Hall of Quiet Embers. I would like something artsy that reflects the song. The song is a metaphor so I am not looking for something where doors are the main emphasis for the cover. During my addiction I burned a lot of bridges, hurt a lot of people, hurt myself and my 3 1/2 year old son died in a house fire while I was sitting in a jail cell. So the hall of Quiet Embers song is a battle that I have in my head... sometimes on a daily basis about picking up and using again. So I play the tape of my life in my head of all of the crap that I've created and what I've done. When I do that, it stops me from relapsing, because I know what will happen if I do.

I don't want a photo. I also want my name on the cd to be Nate R. Don't add my last name just the initial. I've attached the link to the song and also another song called Rise Slow. Also that you can get a feel for it. Also disregard the image that's on ViewLoop.

https://www.viewloop-media.test/watch?v=Qm7rTz2KpL0&t=42s

https://www.viewloop-media.test/watch?v=Hn3wEs8YbFc

Target Market(s)

People in Recovery, Sobriety

Industry/Entity Type

Music Download

Font styles to use
Serif

Colors

Requirements
Must have
• A mysterious feel to it.
Nice to have
• The song is about my secret space which is actually inside my mind. It's a place I go to, kind of like a tape I play that in my head that if I relapse, This will happen and that will happen etc... I also want something that will look good on a T-Shirt and Hats etc...
Should not have
• Nothing Gothic and no Photographs.

```html
<!DOCTYPE html>
<html lang="en">
<head>
<meta charset="utf-8">
<title>The Hall of Quiet Embers — Nate R</title>
<link rel="stylesheet" href="https://fonts.googleapis.com/css2?family=Archivo+Black&family=Permanent+Marker&display=swap">
<style>
  :root {
    --plaster: #d4d2cd;
    --plaster-dark: #8e8e88;
    --splash: #fbfbfa;
    --brick: #c07a55;
    --mortar: #cbb59b;
    --title-teal: #127f99;
    --name-red: #d21f27;
  }
  html, body {
    margin: 0;
    padding: 0;
    width: 1200px;
    height: 1200px;
    overflow: hidden;
    background: var(--plaster);
  }
  .cover {
    position: relative;
    width: 1200px;
    height: 1200px;
    overflow: hidden;
  }
  .wall-texture {
    position: absolute;
    inset: 0;
    width: 1200px;
    height: 1200px;
  }
  .album-title {
    position: absolute;
    left: 148px;
    top: 92px;
    margin: 0;
    font-family: "Archivo Black", "Arial Black", sans-serif;
    font-weight: 400;
    font-size: 128px;
    line-height: 160px;
    letter-spacing: 2px;
    color: var(--title-teal);
    text-transform: uppercase;
  }
  .album-title span {
    display: block;
  }
  .artist-name {
    position: absolute;
    left: 438px;
    top: 1020px;
    margin: 0;
    font-family: "Permanent Marker", cursive;
    font-weight: 400;
    font-size: 112px;
    line-height: 1;
    color: var(--name-red);
  }
</style>
</head>
<body>
<main class="cover">
  <svg class="wall-texture" viewBox="0 0 1200 1200" role="img" aria-label="Weathered grey plaster wall with a white paint splash and exposed red brick at the bottom">
    <defs>
      <linearGradient id="plasterTone" x1="0" y1="0" x2="1" y2="1">
        <stop offset="0" stop-color="#a9a8a2"/>
        <stop offset="0.45" stop-color="#d6d4cf"/>
        <stop offset="1" stop-color="#c9c7c1"/>
      </linearGradient>
      <radialGradient id="splashTone" cx="0.5" cy="0.5" r="0.5">
        <stop offset="0" stop-color="#fefefe"/>
        <stop offset="0.75" stop-color="#f6f6f4"/>
        <stop offset="1" stop-color="#f6f6f4" stop-opacity="0"/>
      </radialGradient>
      <linearGradient id="grimeTone" x1="0" y1="0" x2="0" y2="1">
        <stop offset="0" stop-color="#6f716b" stop-opacity="0.55"/>
        <stop offset="1" stop-color="#6f716b" stop-opacity="0"/>
      </linearGradient>
    </defs>
    <rect width="1200" height="1200" fill="url(#plasterTone)"/>
    <rect width="1200" height="320" fill="url(#grimeTone)"/>
    <ellipse cx="460" cy="560" rx="470" ry="470" fill="url(#splashTone)"/>
    <path d="M60 960 C140 935 230 950 300 942 C420 930 520 948 620 936 C720 922 820 930 900 928 C1000 926 1100 940 1200 946 L1200 1200 L60 1200 Z" fill="var(--brick)"/>
  </svg>

  <h1 class="album-title">
    <span>The</span>
    <span>Hall</span>
    <span>of</span>
    <span>Quiet</span>
    <span>Embers</span>
  </h1>

  <p class="artist-name">Nate R</p>
</main>
</body>
</html>
```